Business card for Chiropractic clinics needs reworked / redesigned

The business card in attachment was designed 10 years ago. It is in need of an update.
We have 2 clinics:
VELDHOVE KLINIEK & VELDHOVE KLINIEK NOORD
Only one address needs to be on the card for doctors that only work in one clinic and two addresses need to be on the card for the doctors that work in both clinics.

Target Market(s)

patients/referrers

Industry/Entity Type

Medical

Contact Information for Business Card

Logo (in full or zoomed-in)
Clinic Name
Doctor name and title
clinic address, website, tel, email

Font styles to use
Sans Serif

Colors

Designer to choose colors to be used in the design.

Requirements
Must have
• Good contrast/readability
• We like modern minimalistic designs
• The Bcard needs to project our very high standard of proficiency/professionalism
Should not have
• Not curly
• Not to much colours

```html
<!DOCTYPE html>
<html lang="nl">
<head>
<meta charset="utf-8">
<title>Veldhove Kliniek Noord – Business Card</title>
<link rel="stylesheet" href="https://fonts.googleapis.com/css2?family=Oswald:wght@600&family=Work+Sans:wght@400;500&display=swap">
<style>
  :root {
    --page-bg: #2a2a2a;
    --card-black: #151515;
    --card-black-light: #1f1f1f;
    --ink-white: #ffffff;
    --ink-soft: #e6e6e6;
    --pattern-tone: #262626;
  }
  * { margin: 0; padding: 0; box-sizing: border-box; }
  html, body {
    width: 1200px;
    height: 900px;
    overflow: hidden;
    background: var(--page-bg);
  }
  .canvas {
    width: 1200px;
    height: 900px;
    display: flex;
    flex-direction: column;
    align-items: center;
    justify-content: center;
    gap: 40px;
  }
  .card {
    width: 700px;
    height: 400px;
    background: linear-gradient(135deg, var(--card-black-light), var(--card-black));
    position: relative;
    overflow: hidden;
    color: var(--ink-white);
    font-family: "Work Sans", sans-serif;
  }

  /* Back side */
  .card-back .pattern-field {
    position: absolute;
    inset: 0;
    background: radial-gradient(ellipse at 65% 45%, var(--pattern-tone), var(--card-black) 75%);
  }
  .card-back .brand-mark {
    position: absolute;
    left: 50%;
    top: 50%;
    transform: translate(-50%, -50%);
    display: flex;
    align-items: center;
    gap: 10px;
    font-size: 15px;
    font-weight: 500;
    letter-spacing: 2px;
    white-space: nowrap;
  }

  /* Front side */
  .card-front .brand-mark {
    position: absolute;
    left: 48px;
    top: 50%;
    transform: translateY(-50%);
    width: 150px;
    display: flex;
    align-items: center;
    gap: 10px;
    font-size: 15px;
    font-weight: 500;
    letter-spacing: 2px;
    line-height: 1.35;
  }
  .brand-dot {
    width: 10px;
    height: 10px;
    border-radius: 50%;
    background: var(--ink-white);
    flex: none;
  }
  .divider {
    position: absolute;
    left: 240px;
    top: 95px;
    width: 2px;
    height: 215px;
    background: var(--ink-white);
  }
  .details {
    position: absolute;
    left: 292px;
    top: 92px;
  }
  .person-name {
    font-family: "Oswald", sans-serif;
    font-weight: 600;
    font-size: 30px;
    letter-spacing: 1px;
    line-height: 1;
    text-transform: uppercase;
  }
  .person-title {
    font-size: 16px;
    color: var(--ink-soft);
    margin-top: 4px;
  }
  .clinic-name {
    font-size: 17px;
    font-weight: 500;
    letter-spacing: 1px;
    margin-top: 22px;
  }
  .clinic-address {
    font-size: 17px;
    margin-top: 2px;
  }
  .contact-list {
    list-style: none;
    margin-top: 20px;
    font-size: 17px;
    line-height: 1.45;
  }
  .contact-list li {
    display: flex;
    align-items: center;
    gap: 10px;
  }
  .contact-icon {
    width: 13px;
    height: 13px;
    flex: none;
    fill: none;
    stroke: var(--ink-white);
    stroke-width: 1.6;
  }
</style>
</head>
<body>
<main class="canvas">

  <section class="card card-back" aria-label="Card back">
    <div class="pattern-field" role="img" aria-label="Faint repeated spine symbol pattern in dark grey"></div>
    <div class="brand-mark">
      <span class="brand-dot"></span>
      <span>VELDHOVE KLINIEK</span>
    </div>
  </section>

  <section class="card card-front" aria-label="Card front">
    <div class="brand-mark">
      <span class="brand-dot"></span>
      <span>VELDHOVE KLINIEK</span>
    </div>
    <div class="divider"></div>
    <div class="details">
      <h1 class="person-name">Pieter Vandamme</h1>
      <p class="person-title">chiropractor</p>
      <p class="clinic-name">VELDHOVE KLINIEK NOORD</p>
      <p class="clinic-address">Kerkstraat 41</p>
      <ul class="contact-list">
        <li>
          <svg class="contact-icon" viewBox="0 0 14 14" aria-hidden="true"><path d="M3 1.5 L5 1.5 L6 4.5 L4.5 5.5 Q5.5 8 8.5 9.5 L9.5 8 L12.5 9 L12.5 11 Q12 12.5 10.5 12.5 Q2 11.5 1.5 3.5 Q1.5 1.8 3 1.5 Z"/></svg>
          <span>09 214 68 30</span>
        </li>
        <li>
          <svg class="contact-icon" viewBox="0 0 14 14" aria-hidden="true"><rect x="1" y="3" width="12" height="8.5"/><path d="M1 3 L7 8 L13 3"/></svg>
          <span>info@veldhovekliniek.be</span>
        </li>
        <li>
          <svg class="contact-icon" viewBox="0 0 14 14" aria-hidden="true"><circle cx="7" cy="7" r="5.8"/><ellipse cx="7" cy="7" rx="2.6" ry="5.8"/><path d="M1.2 7 H12.8"/></svg>
          <span>www.veldhovekliniek.be</span>
        </li>
      </ul>
    </div>
  </section>

</main>
</body>
</html>
```